Harbor Business Cards

I need a business card designed with the following information.

Company Name: Harbor Wealth Management
Name: BriAnne Dockery
Title: Executive Assistant
Cell: (555) 555-0173
Direct Line: (555) 555-0148
Email: brianne@harborwmx.com
Address: 20537 W. Marlowe PKWY Ste. B
Brenwick, TX 77390

I have attached the logo.
I would like it in navy blue and silver.
Thanks.

```html
<!DOCTYPE html>
<html lang="en">
<head>
<meta charset="utf-8">
<title>Harbor Wealth Management – Business Card</title>
<link rel="stylesheet" href="https://fonts.googleapis.com/css2?family=Marcellus&family=Montserrat:wght@400;700&display=swap">
<style>
  :root {
    --navy: #0f2140;
    --white: #ffffff;
    --stage: #d6d8db;
    --ink: #13244a;
  }
  * { box-sizing: border-box; margin: 0; padding: 0; }
  html, body { width: 1200px; height: 960px; overflow: hidden; }
  body { background: var(--stage); position: relative; font-family: "Montserrat", sans-serif; }

  .card {
    position: absolute;
    width: 720px;
    height: 412px;
    border-radius: 36px;
  }

  /* Front */
  .card-front {
    left: 80px; top: 60px;
    background: var(--navy);
    color: var(--white);
    display: flex; flex-direction: column; align-items: center; justify-content: center;
    font-family: "Marcellus", serif;
  }
  .brand-mark {
    width: 62px; height: 62px; border-radius: 50%;
    background: var(--white);
    margin-bottom: 34px;
  }
  .brand-name {
    font-size: 46px; letter-spacing: 0.42em; padding-left: 0.42em; line-height: 1;
  }
  .brand-sub {
    margin-top: 14px; font-size: 13px; letter-spacing: 0.36em; padding-left: 0.36em;
  }

  /* Back */
  .card-back {
    left: 400px; top: 488px;
    background: var(--white);
    color: var(--ink);
  }
  .back-brand {
    position: absolute; left: 48px; top: 130px; width: 230px;
    font-family: "Marcellus", serif; font-size: 34px; line-height: 1.15;
    color: var(--navy);
  }
  .divider { position: absolute; left: 300px; top: 60px; width: 24px; height: 292px; }
  .details { position: absolute; left: 356px; top: 66px; }
  .person-name { font-size: 24px; font-weight: 700; color: var(--navy); }
  .person-title { font-size: 18px; margin-top: 2px; }
  .contacts { list-style: none; margin-top: 22px; }
  .contacts li {
    display: flex; align-items: flex-start; gap: 12px;
    font-size: 17px; line-height: 1.35; margin-bottom: 4px;
  }
  .contacts li.address { margin-top: 16px; }
  .contacts svg { width: 16px; height: 16px; flex: none; margin-top: 4px; fill: var(--navy); }
</style>
</head>
<body>

  <section class="card card-front">
    <span class="brand-mark"></span>
    <div class="brand-name">HARBOR</div>
    <div class="brand-sub">WEALTH MANAGEMENT</div>
  </section>

  <section class="card card-back">
    <div class="back-brand">Harbor Wealth Management</div>

    <svg class="divider" viewBox="0 0 24 292" aria-hidden="true">
      <line x1="3" y1="0" x2="3" y2="292" stroke="#0f2140" stroke-width="2"/>
      <line x1="12" y1="0" x2="12" y2="292" stroke="#0f2140" stroke-width="2"/>
      <line x1="21" y1="0" x2="21" y2="292" stroke="#0f2140" stroke-width="2"/>
    </svg>

    <div class="details">
      <div class="person-name">BriAnne Dockery</div>
      <div class="person-title">Executive Assistant</div>
      <ul class="contacts">
        <li>
          <svg viewBox="0 0 16 16" aria-hidden="true"><path d="M3 1l3 3-2 2c1 2 3 4 5 5l2-2 3 3-2 3C7 15 1 9 1 3z"/></svg>
          <span>(555) 555-0173</span>
        </li>
        <li>
          <svg viewBox="0 0 16 16" aria-hidden="true"><path d="M4 0h8a1 1 0 0 1 1 1v14a1 1 0 0 1-1 1H4a1 1 0 0 1-1-1V1a1 1 0 0 1 1-1zm1 2v10h6V2zm3 11a1 1 0 1 0 0 2 1 1 0 0 0 0-2z"/></svg>
          <span>(555) 555-0148</span>
        </li>
        <li>
          <svg viewBox="0 0 16 16" aria-hidden="true"><path d="M0 3h16v1L8 9 0 4zm0 3l8 5 8-5v7H0z"/></svg>
          <span>brianne@harborwmx.com</span>
        </li>
        <li class="address">
          <svg viewBox="0 0 16 16" aria-hidden="true"><path d="M8 0a5.5 5.5 0 0 1 5.5 5.5C13.5 10 8 16 8 16S2.5 10 2.5 5.5A5.5 5.5 0 0 1 8 0zm0 3a2.5 2.5 0 1 0 0 5 2.5 2.5 0 0 0 0-5z"/></svg>
          <span>20537 W. Marlowe PKWY<br>Ste. B, Brenwick, TX 77390</span>
        </li>
      </ul>
    </div>
  </section>

</body>
</html>
```